Book Cover for Lanterns Beyond the Quiet Tide

I need a book cover for a 6 x 9 paperback titled Lanterns Beyond the Quiet Tide Told by Scholars and Souls Dwelling in the Realm past Our Realm. It has to do with consciousness, the mind, incarnation onto Earth, leaving Earth, and the life in the life after this life. I have an idea I'm providing with this description, but I am open to anything that would be striking and stimulating, whether with a book or not. I am the author, T. Dwight Falmer. I've added another background idea to see if anyone can do something with it and I've increased the budget.

```html
<!DOCTYPE html>
<html lang="en">
<head>
<meta charset="utf-8">
<title>Lanterns Beyond the Quiet Tide — Book Cover</title>
<link rel="stylesheet" href="https://fonts.googleapis.com/css2?family=Cinzel:wght@500;600&family=Marcellus&family=Crimson+Text&display=swap">
<style>
  :root {
    --parchment-light: #ecd9b0;
    --parchment-mid: #dcc294;
    --parchment-dark: #b89565;
    --ink: #2e1c0d;
    --spine-dark: #1e0c05;
    --spine-mid: #3a1a0c;
    --leather-dark: #3d1a0d;
    --leather-mid: #6b3119;
    --leather-light: #8a4a26;
    --border-tone: #4c2312;
    --gold: #e6c96a;
    --gold-soft: #d9bc73;
    --cream: #f0e2c4;
  }
  * { margin: 0; padding: 0; box-sizing: border-box; }
  html, body {
    width: 1200px; height: 882px; overflow: hidden; background: #1a0b04;
  }
  .cover {
    position: relative; width: 1200px; height: 882px; overflow: hidden;
  }
  .front-board {
    position: absolute; left: 600px; top: 0; width: 600px; height: 882px;
    background: radial-gradient(ellipse at 55% 50%, var(--leather-mid), var(--border-tone) 70%, #2a1007);
  }
  .front-panel {
    position: absolute; left: 723px; top: 136px; width: 387px; height: 616px;
    background: radial-gradient(ellipse at 50% 40%, var(--leather-light), var(--leather-mid) 55%, var(--leather-dark));
    box-shadow: inset 0 0 30px rgba(0,0,0,.6), 0 0 0 2px #2a1007, 0 0 0 4px rgba(217,188,115,.25);
  }
  .spine {
    position: absolute; left: 505px; top: 0; width: 130px; height: 882px;
    background: linear-gradient(90deg, var(--spine-dark), var(--spine-mid) 45%, var(--spine-dark));
    border-right: 2px solid #120602;
  }
  .spine-text {
    position: absolute; left: 598px; top: 92px;
    writing-mode: vertical-rl;
    font-family: "Cinzel", serif; font-weight: 500; font-size: 19px;
    letter-spacing: 0.5px; color: var(--gold-soft); white-space: nowrap;
    transform: translateX(-50%);
  }
  .spine-text .spine-author { margin-top: 30px; }
  .spine-dot {
    position: absolute; left: 589px; top: 60px; width: 14px; height: 14px;
    border: 1.5px solid var(--gold-soft); border-radius: 50%;
  }
  .back-sheet { position: absolute; left: 0; top: 0; width: 560px; height: 882px; }
  .back-content {
    position: absolute; left: 36px; top: 0; width: 420px; color: var(--ink);
  }
  .back-title {
    margin-top: 56px; text-align: center;
    font-family: "Cinzel", serif; font-weight: 600; font-size: 24px; line-height: 31px;
  }
  .ornament {
    display: block; margin: 0 auto; background: var(--gold);
    border-radius: 50% 50% 40% 40%;
  }
  .back-ornament { width: 70px; height: 30px; margin-top: 30px; background: #b8962f; }
  .back-body {
    margin-top: 30px;
    font-family: "Crimson Text", serif; font-size: 13.6px; line-height: 18.6px;
    text-align: justify; hyphens: auto; text-align-last: center;
  }
  .front-text {
    position: absolute; left: 723px; top: 136px; width: 387px; text-align: center;
    font-family: "Marcellus", serif; color: var(--cream);
    text-shadow: 0 2px 4px rgba(0,0,0,.6);
  }
  .front-title {
    margin-top: 22px; font-size: 84px; line-height: 100px; color: var(--gold);
    text-shadow: 0 2px 0 #7a5a18, 0 4px 8px rgba(0,0,0,.7);
  }
  .front-subtitle { font-size: 30px; line-height: 37px; margin-top: 6px; }
  .divider {
    position: relative; height: 26px; margin: 6px 30px 4px;
  }
  .divider svg { width: 100%; height: 100%; display: block; }
  .front-byline { font-size: 27px; line-height: 37px; }
  .front-ornament { width: 48px; height: 28px; margin-top: 44px; }
  .front-author {
    margin-top: 40px; font-size: 36px; line-height: 48px; letter-spacing: 1px;
  }
</style>
</head>
<body>
<main class="cover">
  <div class="front-board" role="img" aria-label="Tooled leather book board with an embossed ornamental border and brass corner studs"></div>
  <div class="front-panel"></div>

  <div class="spine"></div>
  <div class="spine-dot"></div>
  <div class="spine-text">
    <span class="spine-title">LANTERNS BEYOND THE QUIET TIDE TOLD</span>
    <span class="spine-author">T. DWIGHT FALMER</span>
  </div>

  <svg class="back-sheet" viewBox="0 0 560 882" aria-hidden="true">
    <defs>
      <linearGradient id="parchment" x1="0" y1="0" x2="1" y2="1">
        <stop offset="0" stop-color="#e9d4a7"/>
        <stop offset="0.5" stop-color="#ecdbb4"/>
        <stop offset="1" stop-color="#cfb080"/>
      </linearGradient>
    </defs>
    <path fill="url(#parchment)" stroke="#6a4520" stroke-width="2"
      d="M0 0 H520 L514 30 L524 62 L512 95 L522 130 L510 168 L519 205 L508 240 L516 280 L506 318 L515 356 L507 395 L513 432 L504 470 L512 510 L503 548 L511 590 L502 630 L510 668 L500 706 L508 746 L499 784 L507 822 L498 860 L504 882 H0 Z"/>
  </svg>

  <section class="back-content">
    <h2 class="back-title">Lanterns Beyond the Quiet<br>Tide Told by Scholars and<br>Souls Dwelling in the Realm<br>past Our Realm</h2>
    <span class="ornament back-ornament" role="img" aria-label="Gold fleur-de-lis ornament"></span>
    <p class="back-body">Lorem ipsum dolor sit amet, consectetur adipisicing elit, sed do eiusmod tempor incididunt ut labore et dolore magna aliqua. Ut enim ad minim veniam, quis nostrud exercitation ullamco laboris nisi ut aliquip ex ea commodo consequat. Duis aute irure dolor in reprehenderit in voluptate velit esse cillum dolore eu fugiat nulla pariatur. Excepteur sint occaecat cupidatat non proident, sunt in culpa qui officia deserunt mollit anim id est laborum. Sed ut perspiciatis unde omnis iste natus error sit voluptatem accusantium doloremque laudantium, totam rem aperiam, eaque ipsa quae ab illo inventore veritatis et quasi architecto beatae vitae dicta sunt explicabo. Nemo enim ipsam voluptatem quia voluptas sit aspernatur aut odit aut fugit, sed quia consequuntur magni dolores eos qui ratione voluptatem sequi nesciunt. Neque porro quisquam est, qui dolorem ipsum quia dolor sit amet, consectetur, adipisci velit, sed quia non numquam eius modi tempora incidunt ut labore et dolore magnam aliquam quaerat voluptatem.</p>
  </section>

  <section class="front-text">
    <h1 class="front-title">Lanterns</h1>
    <p class="front-subtitle">Beyond the Quiet Tide<br>Told</p>
    <div class="divider">
      <svg viewBox="0 0 327 26" preserveAspectRatio="none" aria-hidden="true">
        <line x1="18" y1="13" x2="105" y2="13" stroke="#d9bc73" stroke-width="1.5"/>
        <line x1="222" y1="13" x2="309" y2="13" stroke="#d9bc73" stroke-width="1.5"/>
        <ellipse cx="10" cy="13" rx="9" ry="6" fill="#d9bc73"/>
        <ellipse cx="317" cy="13" rx="9" ry="6" fill="#d9bc73"/>
      </svg>
    </div>
    <p class="front-byline">by Scholars and Souls<br>Dwelling in the Realm<br>past Our Realm</p>
    <span class="ornament front-ornament" role="img" aria-label="Gold fleur-de-lis ornament"></span>
    <p class="front-author">T. DWIGHT<br>FALMER</p>
  </section>
</main>
</body>
</html>
```